依頼詳細
酵素サプリメント「ゆらぎ草の雫」は定期的に酵素浴に通われているお客様をターゲットにしています。週に1回~月に1回程度通われていて、毎日酵素浴したいけれど忙しくて通えない方が代わりにサプリメントを飲むことを想定しています。
記載項目
サイズW120㎜×H190㎜ 裏面記載事項エクセルデータあり。
希望イメージ
シンプル 複雑
単色 カラフル
暗い 明るい
日常 高級
遊び心 厳粛
未来的 伝統的
女性的 男性的
希望する色
茶系
納品ファイル
• 高解像度JPG (.jpg)
• イラストレーター形式 (.ai)
• PNG形式 (.png)
補足説明
和風でシンプルなデザイン希望。茶系に艶消しのシルバー文字をイメージしています。

茶色とベージュ色が波型に入り混じるところがサプリメントによって体が変わっていく様を想起させる点。

当選決定が遅れまして申し訳ございません。皆様からの提案が素晴らしいものばかりで選ぶことができず、いろいろな方の意見を聞いておりました。1つを選ぶのが心苦しいのでコンペはいつも悩みます。これもいつも素晴らしい作品を提案してくださっている皆様方のおかげと感謝しております。
ありがとうございました。

```html
<!DOCTYPE html>
<html lang="ja">
<head>
<meta charset="utf-8">
<title>ゆらぎ草の雫 パッケージ</title>
<link href="https://fonts.googleapis.com/css2?family=Shippori+Mincho:wght@500;700&display=swap" rel="stylesheet">
<style>
  :root {
    --brown: #6d5048;
    --silver: #c9c9cb;
    --silver-light: #eeeeef;
    --silver-dark: #9c9ca0;
    --white: #f6f4f2;
  }
  html, body {
    margin: 0;
    padding: 0;
    width: 874px;
    height: 1200px;
    overflow: hidden;
    background: var(--brown);
  }
  .package {
    position: relative;
    width: 874px;
    height: 1200px;
    background: var(--brown);
    font-family: "Shippori Mincho", serif;
    color: var(--silver);
    overflow: hidden;
  }
  .tagline {
    position: absolute;
    left: 588px;
    top: 70px;
    width: 50px;
    height: 270px;
    border: 2px solid var(--silver);
    box-sizing: border-box;
    writing-mode: vertical-rl;
    display: flex;
    align-items: center;
    justify-content: center;
    font-size: 24px;
    font-weight: 500;
    letter-spacing: 3px;
    color: var(--white);
  }
  .title-lead {
    position: absolute;
    left: 140px;
    top: 220px;
    font-size: 130px;
    font-weight: 700;
    line-height: 1;
    color: var(--white);
    letter-spacing: -4px;
    white-space: nowrap;
  }
  .title-char {
    position: absolute;
    font-size: 122px;
    font-weight: 700;
    line-height: 1;
    background: linear-gradient(160deg, var(--silver-light), var(--silver) 50%, var(--silver-dark));
    -webkit-background-clip: text;
    background-clip: text;
    color: transparent;
  }
  .title-char.first { left: 150px; top: 400px; }
  .title-char.second { left: 272px; top: 545px; }
  .title-char.third { left: 150px; top: 700px; }
  .emblem {
    position: absolute;
    left: 430px;
    top: 480px;
    width: 440px;
    height: 400px;
  }
  .brand {
    position: absolute;
    left: 78px;
    top: 1010px;
    display: flex;
    align-items: center;
    gap: 12px;
    color: var(--white);
  }
  .brand-dot {
    width: 44px;
    height: 44px;
    border-radius: 50%;
    background: var(--white);
  }
  .brand-name {
    font-size: 28px;
    font-weight: 500;
    letter-spacing: 2px;
  }
  .count {
    position: absolute;
    right: 70px;
    bottom: 60px;
    font-size: 28px;
    font-weight: 500;
    color: var(--white);
  }
</style>
</head>
<body>
<div class="package">
  <div class="tagline">おうちで摂れる酵素</div>

  <div class="title-lead">ゆらぎ</div>
  <div class="title-char first">草</div>
  <div class="title-char second">の</div>
  <div class="title-char third">雫</div>

  <svg class="emblem" viewBox="0 0 440 400">
    <defs>
      <linearGradient id="silverStroke" x1="0" y1="0" x2="1" y2="1">
        <stop offset="0" stop-color="#f0f0f1"/>
        <stop offset="0.5" stop-color="#c4c4c7"/>
        <stop offset="1" stop-color="#8f8f94"/>
      </linearGradient>
      <radialGradient id="bubbleFill" cx="0.4" cy="0.4" r="0.7">
        <stop offset="0" stop-color="#e9e9eb"/>
        <stop offset="0.6" stop-color="#b9b9bd"/>
        <stop offset="1" stop-color="#8a7873"/>
      </radialGradient>
    </defs>
    <polygon points="20,200 120,24 320,24 420,200 320,376 120,376"
             fill="none" stroke="url(#silverStroke)" stroke-width="14"/>
    <polygon points="44,200 134,44 306,44 396,200 306,356 134,356"
             fill="url(#bubbleFill)" role="img" aria-label="泡が重なり合うモチーフ"/>
  </svg>

  <div class="brand">
    <span class="brand-dot"></span>
    <span class="brand-name">森野酵素</span>
  </div>

  <div class="count">60粒</div>
</div>
</body>
</html>
```